New Zealand Marlborough Sauvignon Blanc wine packaging design

We need packaging design for our new wine brand, Dunmore Hale. The wine is a New Zealand Marlborough Sauvignon Blanc. We would like the packaging will portray elegance and style with an understated label. We are looking for a label that portrays the elegance of the French Riviera. The label should be round or pill shaped.
Updates

Industry/Entity Type

Wine

Font styles to use
Serif
Sans Serif

Requirements
Must have
• The words in order of importance: Dunmore Hale, Sauvignon Blanc, Marlborough, New Zealand. It should be fit to the bottle posted in the links
Nice to have
• a pill shape or circular shape
Should not have
• Illustrations of wine bottles, wine glasses, or grapes

```html
<!DOCTYPE html>
<html lang="en">
<head>
<meta charset="utf-8">
<title>Dunmore Hale – Marlborough Sauvignon Blanc Label</title>
<link rel="stylesheet" href="https://fonts.googleapis.com/css2?family=Rye&family=Montserrat:wght@700&family=Josefin+Sans:wght@600&family=Libre+Baskerville&family=Lato:wght@400&display=swap">
<style>
  :root {
    --page-bg: #000000;
    --ink: #111111;
    --paper: #ffffff;
    --cream: #f7efd2;
    --cream-deep: #e9dcb0;
    --gold-light: #fff3b8;
    --gold-mid: #e8c04a;
    --gold-deep: #b98a1c;
  }
  html, body {
    margin: 0;
    padding: 0;
    width: 773px;
    height: 1200px;
    overflow: hidden;
    background: var(--page-bg);
  }
  .label-sheet {
    width: 773px;
    height: 1200px;
    display: flex;
    align-items: center;
    justify-content: center;
    gap: 46px;
  }
  .label { display: block; }
  .label--mono { width: 300px; height: 371px; }
  .label--gold { width: 340px; height: 420px; }
  .brand-arc {
    font-family: "Rye", serif;
    font-size: 29px;
    letter-spacing: 1px;
  }
  .region-name {
    font-family: "Montserrat", sans-serif;
    font-weight: 700;
    font-size: 25px;
    letter-spacing: 1px;
  }
  .variety-name {
    font-family: "Josefin Sans", sans-serif;
    font-weight: 600;
    font-size: 23px;
    letter-spacing: 0.5px;
  }
  .vintage {
    font-family: "Libre Baskerville", serif;
    font-size: 19px;
  }
  .origin-arc {
    font-family: "Lato", sans-serif;
    font-size: 19px;
    letter-spacing: 0.5px;
  }
</style>
</head>
<body>
<main class="label-sheet">

  <!-- Monochrome label -->
  <svg class="label label--mono" viewBox="0 0 340 420" xmlns="http://www.w3.org/2000/svg">
    <defs>
      <path id="mono-top-path" d="M50,185 A120 120 0 0 1 290,185"/>
      <path id="mono-bottom-path" d="M38,250 A132 132 0 0 0 302,250"/>
      <clipPath id="mono-shape"><ellipse cx="170" cy="210" rx="160" ry="205"/></clipPath>
    </defs>
    <g clip-path="url(#mono-shape)">
      <ellipse cx="170" cy="210" rx="160" ry="205" fill="var(--paper)"/>
      <rect class="scene-fill" role="img" aria-label="Fine line sketch of a hillside above a coastal village" x="0" y="40" width="340" height="330" fill="#eeeeee"/>
      <path class="brand-band" d="M22,185 A148 148 0 0 1 318,185 L282,185 A112 112 0 0 0 58,185 Z" fill="var(--paper)" stroke="var(--ink)" stroke-width="2.5"/>
      <text class="brand-arc" fill="var(--ink)"><textPath href="#mono-top-path" startOffset="50%" text-anchor="middle">DUNMORE HALE</textPath></text>
      <rect class="title-band" x="0" y="196" width="340" height="74" fill="var(--ink)"/>
      <text class="region-name" x="170" y="228" text-anchor="middle" fill="var(--paper)">MARLBOROUGH</text>
      <text class="variety-name" x="170" y="259" text-anchor="middle" fill="var(--paper)">SAUVIGNON BLANC</text>
      <path class="origin-band" d="M34.4,285 A140 140 0 0 0 305.6,285 Z" fill="var(--paper)" stroke="var(--ink)" stroke-width="2.5"/>
      <path class="vintage-cap" d="M72.1,285 A104 104 0 0 0 267.9,285 Z" fill="var(--paper)" stroke="var(--ink)" stroke-width="2"/>
      <text class="vintage" x="170" y="318" text-anchor="middle" fill="var(--ink)">2023</text>
      <text class="origin-arc" fill="var(--ink)"><textPath href="#mono-bottom-path" startOffset="50%" text-anchor="middle">WINE OF NEW ZEALAND</textPath></text>
    </g>
    <ellipse cx="170" cy="210" rx="159" ry="204" fill="none" stroke="var(--ink)" stroke-width="1.5"/>
  </svg>

  <!-- Gold label -->
  <svg class="label label--gold" viewBox="0 0 340 420" xmlns="http://www.w3.org/2000/svg">
    <defs>
      <linearGradient id="gold-frame" x1="0" y1="0" x2="1" y2="1">
        <stop offset="0" stop-color="var(--gold-deep)"/>
        <stop offset="0.35" stop-color="var(--gold-light)"/>
        <stop offset="0.65" stop-color="var(--gold-mid)"/>
        <stop offset="1" stop-color="var(--gold-deep)"/>
      </linearGradient>
      <linearGradient id="gold-band" x1="0" y1="0" x2="1" y2="0">
        <stop offset="0" stop-color="var(--gold-mid)"/>
        <stop offset="0.5" stop-color="var(--gold-light)"/>
        <stop offset="1" stop-color="var(--gold-mid)"/>
      </linearGradient>
      <radialGradient id="cream-field" cx="0.5" cy="0.45" r="0.6">
        <stop offset="0" stop-color="var(--cream)"/>
        <stop offset="1" stop-color="var(--cream-deep)"/>
      </radialGradient>
      <path id="gold-top-path" d="M50,185 A120 120 0 0 1 290,185"/>
      <path id="gold-bottom-path" d="M38,250 A132 132 0 0 0 302,250"/>
      <clipPath id="gold-inner"><rect x="14" y="14" width="312" height="392" rx="156"/></clipPath>
    </defs>
    <rect class="frame" x="0" y="0" width="340" height="420" rx="170" fill="url(#gold-frame)"/>
    <g clip-path="url(#gold-inner)">
      <rect class="scene-fill" role="img" aria-label="Fine line sketch of a hillside above a coastal village" x="14" y="14" width="312" height="392" fill="url(#cream-field)"/>
      <path class="brand-band" d="M22,185 A148 148 0 0 1 318,185 L282,185 A112 112 0 0 0 58,185 Z" fill="var(--ink)" stroke="var(--paper)" stroke-width="1.5"/>
      <text class="brand-arc" fill="var(--paper)"><textPath href="#gold-top-path" startOffset="50%" text-anchor="middle">DUNMORE HALE</textPath></text>
      <rect class="title-band" x="14" y="196" width="312" height="74" fill="url(#gold-band)"/>
      <text class="region-name" x="170" y="228" text-anchor="middle" fill="var(--ink)">MARLBOROUGH</text>
      <text class="variety-name" x="170" y="259" text-anchor="middle" fill="var(--ink)">SAUVIGNON BLANC</text>
      <path class="origin-band" d="M34.4,285 A140 140 0 0 0 305.6,285 Z" fill="var(--ink)"/>
      <path class="vintage-cap" d="M72.1,285 A104 104 0 0 0 267.9,285 Z" fill="var(--ink)" stroke="var(--paper)" stroke-width="1.5"/>
      <text class="vintage" x="170" y="318" text-anchor="middle" fill="var(--paper)">2023</text>
      <text class="origin-arc" fill="var(--paper)"><textPath href="#gold-bottom-path" startOffset="50%" text-anchor="middle">WINE OF NEW ZEALAND</textPath></text>
    </g>
  </svg>

</main>
</body>
</html>
```